Homemaking training schools needs a Business Card design

Designer, Hello!

No special requirements, good-looking enough.
--------------------------------------------------------------------------

Name: Marcus Liao
Chairman
Tel: 0574-57418263
Mobile: 13852247106
Email: kelvory@mailpond.com
Web: www.tqb2031.com
Add: No.258, LinfengJie, DaoyueQu, Ningbo, Zhejiang

LOGO
Ningbo TQB Homemaking Training School

Target Market(s)

pregnant women, mothers, infants, the elderly and families, including cleaning, cooking, nursing training.

Industry/Entity Type

Business

Contact Information for Business Card

Name: Marcus Liao
Chairman
Tel: 0574-57418263
Mobile: 13852247106
Email: kelvory@mailpond.com
Web: www.tqb2031.com

LOGO

Font styles to use
Serif
Sans Serif
Decorative

Requirements
Nice to have
• Feels: clean, specifications, safety, comfort, warmth and happiness.

```html
<!DOCTYPE html>
<html lang="en">
<head>
<meta charset="utf-8">
<title>TianQingBao Business Card</title>
<link rel="stylesheet" href="https://fonts.googleapis.com/css2?family=Raleway:wght@400;500;700&display=swap">
<style>
  :root {
    --page: #e4e2df;
    --card: #221f20;
    --blue: #0b6fbf;
    --pink: #e4007f;
    --slate: #4a5468;
    --text: #ffffff;
    --line: #cfd3da;
  }
  * { margin: 0; padding: 0; box-sizing: border-box; }
  html, body { width: 1200px; height: 900px; overflow: hidden; }
  body {
    background: var(--page);
    font-family: "Raleway", sans-serif;
    color: var(--text);
    position: relative;
  }
  .card {
    position: absolute;
    left: 280px;
    width: 640px;
    height: 384px;
    background: var(--card);
    overflow: hidden;
    box-shadow: 0 10px 30px rgba(0,0,0,.25);
  }
  .card-front { top: 44px; }
  .card-back { top: 472px; }
  .card-art { position: absolute; inset: 0; }

  .brand { position: absolute; text-align: center; }
  .brand-name {
    font-weight: 700;
    color: var(--blue);
    letter-spacing: .5px;
    line-height: 1;
  }
  .brand-tag {
    display: flex;
    align-items: center;
    gap: 6px;
    font-weight: 400;
    color: var(--line);
    margin-top: 5px;
    white-space: nowrap;
  }
  .brand-tag::before, .brand-tag::after {
    content: "";
    flex: 1;
    height: 1px;
    background: var(--line);
  }
  .card-front .brand { left: 0; right: 0; top: 148px; width: 300px; margin: 0 auto; }
  .card-front .brand-name { font-size: 38px; }
  .card-front .brand-tag { font-size: 13px; }

  .card-back .brand { left: 64px; top: 296px; width: 220px; }
  .card-back .brand-name { font-size: 28px; }
  .card-back .brand-tag { font-size: 11px; }

  .person { position: absolute; left: 66px; top: 34px; }
  .person-name { font-size: 27px; font-weight: 400; letter-spacing: 1.5px; text-transform: uppercase; }
  .person-title { font-size: 20px; color: var(--blue); font-weight: 400; margin-top: 2px; }

  .contacts { position: absolute; left: 62px; top: 112px; list-style: none; }
  .contacts li {
    display: flex;
    align-items: center;
    gap: 12px;
    font-size: 19px;
    height: 26px;
    margin-bottom: 2px;
  }
  .contacts svg { width: 20px; height: 20px; flex: none; }

  .address-band {
    position: absolute;
    left: 0; right: 0; top: 236px;
    height: 32px;
    background: var(--blue);
    font-size: 18px;
    line-height: 32px;
    padding-left: 78px;
    white-space: nowrap;
  }
</style>
</head>
<body>

<section class="card card-front" aria-label="Card front">
  <svg class="card-art" viewBox="0 0 640 384" aria-hidden="true">
    <circle cx="0" cy="190" r="118" fill="var(--blue)"/>
    <circle cx="0" cy="200" r="36" fill="var(--pink)"/>
    <circle cx="18" cy="0" r="44" fill="var(--pink)"/>
    <circle cx="640" cy="200" r="104" fill="var(--blue)"/>
    <circle cx="640" cy="210" r="34" fill="var(--pink)"/>
    <circle cx="626" cy="14" r="40" fill="var(--pink)"/>
  </svg>
  <div class="brand">
    <div class="brand-name">TianQingBao</div>
    <div class="brand-tag">Training &amp; Services</div>
  </div>
</section>

<section class="card card-back" aria-label="Card back">
  <svg class="card-art" viewBox="0 0 640 384" aria-hidden="true">
    <circle cx="600" cy="190" r="210" fill="var(--slate)" opacity=".75"/>
    <circle cx="640" cy="120" r="160" fill="#5a6478" opacity=".55"/>
    <circle cx="640" cy="560" r="270" fill="var(--slate)" opacity=".8"/>
  </svg>

  <div class="person">
    <div class="person-name">Marcus Liao</div>
    <div class="person-title">Chairman</div>
  </div>

  <ul class="contacts">
    <li>
      <svg viewBox="0 0 20 20" fill="none" stroke="var(--blue)" stroke-width="1.5"><circle cx="10" cy="10" r="8.5"/><path d="M7 5.5l1.5 2-1 1.2c.7 1.5 1.8 2.6 3.3 3.3l1.2-1 2 1.5-.8 1.6c-3.5-.3-6.5-3.3-6.8-6.8z"/></svg>
      0574-57418263
    </li>
    <li>
      <svg viewBox="0 0 20 20" fill="none" stroke="var(--blue)" stroke-width="1.5"><circle cx="10" cy="10" r="8.5"/><rect x="7" y="5" width="6" height="10" rx="1"/><path d="M9.3 13h1.4"/></svg>
      13852247106
    </li>
    <li>
      <svg viewBox="0 0 20 20" fill="none" stroke="var(--blue)" stroke-width="1.5"><rect x="2" y="5" width="16" height="11"/><path d="M2 5l8 6 8-6M2 16l6-5M18 16l-6-5"/></svg>
      kelvory@mailpond.com
    </li>
    <li>
      <svg viewBox="0 0 20 20" fill="none" stroke="var(--blue)" stroke-width="1.5"><circle cx="10" cy="10" r="8.5"/><path d="M1.5 10h17M10 1.5c-3 3-3 14 0 17M10 1.5c3 3 3 14 0 17"/></svg>
      www.tqb2031.com
    </li>
  </ul>

  <div class="address-band">No.258, LinfengJie, DaoyueQu, Ningbo, Zhejiang</div>

  <div class="brand">
    <div class="brand-name">TianQingBao</div>
    <div class="brand-tag">Training &amp; Services</div>
  </div>
</section>

</body>
</html>
```